Surface Protection company needs cards

We are a New Zealand company that will apply nanotechnology coatings on surfaces to prevent growth and spread of bacteria, viruses, mold etc with a sprayer. We deal with large corporates, airlines, hospitals and schools so we are after a new modern, simple and clean look that will have great visual impact.
We a company that is focused on prevention and protection.

Company name, Vela Shield

Subtext, Antimicrobial Surface Protection

Logo, VS

Target Market(s)

Hospitals, Transport agencies, Airlines, Corporate entities

Contact Information for Business Card

Company name, VelaShield
Logo, VS

Gareth Tolley
velashieldnz@postbox.example
+64219305562
www.velashield.example.nz

Requirements
Must have
• Simple clean look.
Nice to have
• We apply nano coatings so try and incorporate this into a theme somehow

```html
<!DOCTYPE html>
<html lang="en">
<head>
<meta charset="utf-8">
<title>Vela Shield – Business Cards</title>
<link href="https://fonts.googleapis.com/css2?family=Montserrat:wght@400;700&family=Raleway:wght@400;500&display=swap" rel="stylesheet">
<style>
  :root {
    --bg: #dfeaec;
    --card-dark: #323035;
    --card-light: #ffffff;
    --brand-blue: #4a9fd8;
    --brand-green: #5aad2f;
    --ink: #2e2e30;
    --muted: #8a8a8e;
    --rule: #555558;
  }
  * { margin: 0; padding: 0; box-sizing: border-box; }
  html, body { width: 717px; height: 1200px; overflow: hidden; }
  body { background: var(--bg); position: relative; font-family: "Raleway", sans-serif; }

  .card {
    position: absolute; left: 58px; width: 600px; height: 338px;
    border-radius: 17px; overflow: hidden;
  }
  .card svg.bands { position: absolute; inset: 0; }

  /* Front */
  .card--front { top: 170px; background: var(--card-dark); }
  .brand { position: absolute; left: 0; right: 0; text-align: center; }
  .brand__name {
    display: inline-flex; align-items: center; gap: 12px;
    font-family: "Montserrat", sans-serif; font-weight: 700;
    color: var(--brand-blue); letter-spacing: 0.5px; line-height: 1;
  }
  .brand__dot { border-radius: 50%; background: var(--brand-green); display: inline-block; }
  .card--front .brand__name { font-size: 37px; }
  .card--front .brand__dot { width: 16px; height: 16px; }
  .card--front .brand { top: 140px; }
  .card--front .tagline {
    position: absolute; top: 194px; left: 0; right: 0; text-align: center;
    font-family: "Montserrat", sans-serif; font-size: 12px; letter-spacing: 1.6px;
    color: var(--muted);
  }
  .card--front .website {
    position: absolute; top: 264px; left: 0; right: 0; text-align: center;
    font-family: "Raleway", sans-serif; font-size: 13px; color: #f2f2f2;
  }

  /* Back */
  .card--back { top: 690px; background: var(--card-light); }
  .person { position: absolute; left: 56px; top: 48px; }
  .person__name {
    font-family: "Montserrat", sans-serif; font-weight: 700; font-size: 27px;
    color: var(--brand-blue); line-height: 1;
  }
  .person__role { font-size: 14px; color: var(--muted); margin-top: 6px; }
  .person__rule { width: 119px; height: 1px; background: var(--rule); margin-top: 6px; }

  .contacts { position: absolute; left: 56px; top: 126px; list-style: none; }
  .contacts li { display: flex; align-items: center; height: 24px; margin-bottom: 7px; }
  .contacts .icon {
    width: 24px; height: 24px; border-radius: 3px; background: var(--brand-blue);
    display: flex; align-items: center; justify-content: center; flex: none;
  }
  .contacts span { margin-left: 18px; font-size: 13px; color: var(--ink); }

  .card--back .brand { left: 344px; right: 16px; top: 168px; }
  .card--back .brand__name { font-size: 26px; gap: 9px; }
  .card--back .brand__dot { width: 11px; height: 11px; }
  .card--back .tagline {
    position: absolute; left: 344px; right: 16px; top: 200px; text-align: center;
    font-family: "Montserrat", sans-serif; font-size: 8.5px; letter-spacing: 0.9px; color: var(--muted);
  }
</style>
</head>
<body>

<section class="card card--front" aria-label="Card front">
  <svg class="bands" width="600" height="338" viewBox="0 0 600 338" aria-hidden="true">
    <polygon points="191,0 408,0 401,13 198,13" fill="var(--brand-blue)"/>
    <polygon points="0,260 149,260 169,294 0,294" fill="var(--brand-blue)"/>
    <polygon points="449,260 600,260 600,294 430,294" fill="var(--brand-green)"/>
  </svg>
  <div class="brand"><span class="brand__name"><i class="brand__dot"></i>VELA SHIELD</span></div>
  <p class="tagline">ANTIMICROBIAL SURFACE PROTECTION</p>
  <p class="website">www.velashield.example.nz</p>
</section>

<section class="card card--back" aria-label="Card back">
  <svg class="bands" width="600" height="338" viewBox="0 0 600 338" aria-hidden="true">
    <polygon points="0,271 391,271 372,305 0,305" fill="var(--brand-blue)"/>
    <polygon points="410,271 600,271 600,305 389,305" fill="var(--brand-green)"/>
  </svg>

  <div class="person">
    <h1 class="person__name">GARETH TOLLEY</h1>
    <p class="person__role">Solution Manager</p>
    <div class="person__rule"></div>
  </div>

  <ul class="contacts">
    <li>
      <i class="icon"><svg width="14" height="14" viewBox="0 0 14 14"><path d="M7 1a4.2 4.2 0 0 0-4.2 4.2C2.8 8.4 7 13 7 13s4.2-4.6 4.2-7.8A4.2 4.2 0 0 0 7 1z" fill="none" stroke="#fff" stroke-width="1.5"/><circle cx="7" cy="5.2" r="1.5" fill="#fff"/></svg></i>
      <span>Harbour Lane, Wellington, NZ.</span>
    </li>
    <li>
      <i class="icon"><svg width="14" height="14" viewBox="0 0 14 14"><path d="M2 2l10 4.5-4.2 1.3L6.5 12z" fill="#fff"/></svg></i>
      <span>velashieldnz@postbox.example</span>
    </li>
    <li>
      <i class="icon"><svg width="14" height="14" viewBox="0 0 14 14"><path d="M3.2 1.5l2 2.6-1.1 1.4c.8 1.7 2.2 3.1 3.9 3.9l1.4-1.1 2.6 2-1.2 2.2C6.3 12.3 1.7 7.7 1 2.7z" fill="#fff"/></svg></i>
      <span>+64219305562</span>
    </li>
    <li>
      <i class="icon"><svg width="14" height="14" viewBox="0 0 14 14"><circle cx="7" cy="7" r="5.3" fill="none" stroke="#fff" stroke-width="1.3"/><ellipse cx="7" cy="7" rx="2.3" ry="5.3" fill="none" stroke="#fff" stroke-width="1"/><line x1="1.7" y1="7" x2="12.3" y2="7" stroke="#fff" stroke-width="1"/></svg></i>
      <span>www.velashield.example.nz</span>
    </li>
  </ul>

  <div class="brand"><span class="brand__name"><i class="brand__dot"></i>VELA SHIELD</span></div>
  <p class="tagline">ANTIMICROBIAL SURFACE PROTECTION</p>
</section>

</body>
</html>
```